Selvin: A Friday night in the Prophetic Flyer

We are holding 2 Friday night events, one on 10/25/19 and the other on 11/29/19.
The time frame is 6:30pm-9:00pm. These services will be a time of prayer/healing for the sick and will be prophetic as well. (There will be prophets prophesying over people)

The event is called: Selvin: A Friday night in the Prophetic
The flyer should also include the phrase/excerpt: "And they prophesied also".

Keywords/Phrases: Prophetic, Healing, Climbing in the Spirit, Higher level of Anointing...

Target Market(s)

those looking for healing, seeking a word from God

Colors

Designer to choose colors to be used in the design.

Requirements
Must have
• The event is called: Selvin: A Friday night in the Prophetic
• The flyer should also include the phrase/excerpt: "And they prophesied also".
• It must include the Tovik logo attached, either is fine, we have attached two different versions.
• It must have the dates, location, time
• Dates: October 25, 2019 and November 29, 2019
• Location: Hollard Community Center
• (Downtown Portland) 482 Wendle Street
• Portland, ME 04102
• Time: 6:30pm-9:00pm
• Contact Info: Tel. 207-555-3841
• email: contact@brimfield-hall.org
• web: www.tovik.org
Nice to have
• creativity in color scheme, the meaning of the word Selvin conveyed in a classy artistic way/design.
Should not have
• Crosses, pictures of churches

```html
<!DOCTYPE html>
<html lang="en">
<head>
<meta charset="utf-8">
<title>Selvin: A Friday night in the Prophetic</title>
<link href="https://fonts.googleapis.com/css2?family=Cinzel:wght@900&family=Montserrat:wght@500;600;800&family=Courier+Prime:wght@700&family=Oswald:wght@500&family=Roboto:wght@400&display=swap" rel="stylesheet">
<style>
  :root {
    --stage: #d6d6d6;
    --ink: #000000;
    --orange: #f7941d;
    --white: #ffffff;
    --sky-dark: #1b2130;
    --sky-mid: #4a5468;
    --sun: #f3d3bf;
  }
  * { margin: 0; padding: 0; box-sizing: border-box; }
  html, body { width: 703px; height: 1200px; overflow: hidden; background: var(--stage); }
  .flyer {
    position: absolute; left: 22px; top: 133px; width: 660px; height: 933px;
    background: var(--ink); box-shadow: 8px 8px 10px rgba(0,0,0,.35); overflow: hidden;
  }
  .flyer > * { position: absolute; }
  .event-title {
    left: 0; width: 100%; top: 30px; text-align: center;
    font-family: "Cinzel", serif; font-weight: 900; font-size: 100px; line-height: 1;
    color: var(--orange); letter-spacing: 1px;
  }
  .event-subtitle {
    left: 0; width: 100%; top: 130px; text-align: center;
    font-family: "Montserrat", sans-serif; font-weight: 600; font-size: 29px; color: var(--white);
  }
  .divider {
    left: 170px; width: 328px; top: 181px; height: 2px;
    background: linear-gradient(90deg, transparent, var(--orange) 20%, var(--orange) 80%, transparent);
  }
  .scripture {
    left: 0; width: 100%; top: 191px; text-align: center;
    font-family: "Courier Prime", monospace; font-weight: 700; font-size: 19px;
    color: var(--white); letter-spacing: 2px;
  }
  .hero-photo {
    left: 0; top: 220px; width: 660px; height: 464px;
    background:
      radial-gradient(circle at 77% 37%, var(--sun) 0, #c98f7a 6%, rgba(120,90,100,.6) 16%, transparent 34%),
      linear-gradient(180deg, #000 0%, var(--sky-dark) 12%, var(--sky-mid) 45%, #2a2b2e 72%, #12140f 88%, #000 100%);
  }
  .dates {
    left: 40px; width: 264px; top: 697px; text-align: right;
    font-family: "Montserrat", sans-serif; font-weight: 800; font-size: 30px; line-height: 34px;
    color: var(--white);
  }
  .year-tag {
    left: 317px; top: 697px; width: 32px; height: 72px; background: var(--orange);
    display: flex; align-items: center; justify-content: center;
  }
  .year-tag span {
    transform: rotate(-90deg); font-family: "Montserrat", sans-serif; font-weight: 800;
    font-size: 21px; color: var(--ink);
  }
  .time {
    left: 362px; top: 696px; font-family: "Oswald", sans-serif; font-weight: 500;
    font-size: 29px; line-height: 34px; color: var(--white);
  }
  .venue {
    left: 362px; top: 729px; font-family: "Roboto", sans-serif; font-size: 12.5px;
    line-height: 14px; color: var(--white);
  }
  .brand-name {
    left: 47px; top: 838px; font-family: "Montserrat", sans-serif; font-weight: 600;
    font-size: 44px; line-height: 1; color: var(--white); letter-spacing: 1px;
  }
  .call-box {
    left: 243px; top: 795px; width: 373px; height: 28px;
    border: 1.5px solid var(--white); border-radius: 6px; overflow: hidden; display: flex;
  }
  .call-label {
    width: 149px; background: var(--orange); color: var(--ink); font-family: "Montserrat", sans-serif;
    font-weight: 500; font-size: 19px; line-height: 25px; padding-left: 10px;
    border-radius: 5px 14px 14px 5px;
  }
  .call-number {
    flex: 1; color: var(--white); font-family: "Montserrat", sans-serif; font-weight: 500;
    font-size: 25px; line-height: 25px; padding-left: 12px;
  }
  .contact-box {
    left: 243px; top: 842px; width: 331px; height: 32px;
    border: 1.5px solid var(--white); border-radius: 6px;
    display: flex; align-items: center; gap: 6px; padding-left: 16px;
    font-family: "Roboto", sans-serif; font-size: 13px; color: var(--white);
  }
  .contact-box svg { flex: none; }
  .contact-box .web-icon { margin-left: 10px; }
</style>
</head>
<body>
  <main class="flyer">
    <h1 class="event-title">SELVIN</h1>
    <p class="event-subtitle">A Friday night in the Prophetic</p>
    <div class="divider"></div>
    <p class="scripture">"And they prophesied also"</p>
    <div class="hero-photo" role="img" aria-label="Photo of a man kneeling in prayer in a field beneath a cloudy sky with bright sunlight"></div>
    <p class="dates">OCTOBER 25 &amp;<br>NOVEMBER 29</p>
    <div class="year-tag"><span>2019</span></div>
    <p class="time">6:30PM-9:00PM</p>
    <p class="venue">Hollard Community Center<br>(Downtown Portland) 482 Wendle Street<br>Portland, ME 04102</p>
    <p class="brand-name">Tovik</p>
    <div class="call-box">
      <span class="call-label">Call us now</span>
      <span class="call-number">207-555-3841</span>
    </div>
    <div class="contact-box">
      <svg width="13" height="10" viewBox="0 0 13 10" aria-hidden="true">
        <rect x="0.5" y="0.5" width="12" height="9" fill="var(--orange)"/>
        <path d="M0.5 0.5 L6.5 5.5 L12.5 0.5" fill="none" stroke="var(--ink)" stroke-width="1"/>
      </svg>
      <span>contact@brimfield-hall.org</span>
      <svg class="web-icon" width="13" height="13" viewBox="0 0 13 13" aria-hidden="true">
        <circle cx="6.5" cy="6.5" r="6" fill="var(--orange)"/>
        <path d="M0.5 6.5 H12.5 M6.5 0.5 C3 4 3 9 6.5 12.5 M6.5 0.5 C10 4 10 9 6.5 12.5" fill="none" stroke="var(--ink)" stroke-width="0.9"/>
      </svg>
      <span>www.tovik.org</span>
    </div>
  </main>
</body>
</html>
```